We need a book cover design for a fitness professional's guidebook to be a successful trainer. LA celebrity trainer offers 7 ideas that are designed to transform any fitness professional's career and life. The cover design we are into is attached an includes the image of a man who is half dressed in a business suit and half dressed in fitness gear. The back photo should demonstrate the four sphere's the book is designed around (also attached) and will be included on the back with a brief description of the material (included below) and a short bio and photo of the writer (attached) at the very bottom. We'd like the book to have a work book feel, or text book geometry to it. The brand colors are Black and Red. The final design should invoke the feeling of success, health and happiness.

Dimensions: 8 5/8 x 5 3/4

USE WEBSITE AS REFERENCE FOR BRAND COLORS AND DESIGNS:
BrenoVigor.net

BOOK TITLE:
RISING STRIDE
"A fitness professional's guidebook to be a successful trainer."

BACK COVER COPY:
Celebrity conditioning specialist and trainer consultant, Tavo Minardi, offers powerful ideas that are designed to transform every fitness professional's career and life. Reveal essential tools that every trainer and entrepreneur should know. Discover the deeper meaning of yourself and your career by working smarter rather than harder.

Find out how to create a brand, advertise it, and hone in on your market. Create buzz by landing magazine press. How to build celebrity clientele. Explore the world of multi-media projects. And finally, what to do when you reach your goals. This is an opportunity for trainer's to capture a share of the fitness industry’s vast $27B market. Fulfill your fullest earning potential while also understanding what the true meaning of success is, and how to achieve it. Learn what you love to do, what you do well, what the fitness industry needs and what it will pay for.

Aimed at the trainers who want to know the mistakes to avoid, and the habits to establish that will set them apart from the rest, Rising Stride is THE guidebook that has the power to take your career and life in the direction that will prepare you for continued success. Use these business ideas to promote your passive income, generate multiple streams of revenue and increase your investments, resulting in more freedom and access in the fitness industry and beyond. Let Rising Stride unleash your potential to be a successful trainer.

BACK AUTHOR BIO:
Los Angeles based celebrity trainer and trainer consultant, Tavo Minardi, CSCS, developed his very own “Ember” technique and fitness brand. Minardi’s clients include a mix of celebrities, professional athletes, musicians, fashion models, students, political figures and corporate professionals. Kelvo magazine described Minardi’s fitness DVD, TAVOMOVE, as “a workout you’ll look forward to”. Tavo was also the co-developer of a natural energy drink that increases energy and metabolism with an ancient Peruvian super food. Additionally backed by his finance and advertising education, Tavo has consulted several trainers and fitness brands to guide them to their maximum earning potential.

Target Market(s)

Fitness Industry/Trainers

Industry/Entity Type

Advertising

Requirements
Must have
• Consistent with website logo colors, shapes and fonts.

```html
<!DOCTYPE html>
<html lang="en">
<head>
<meta charset="utf-8">
<title>Rising Stride – Back Cover</title>
<link rel="stylesheet" href="https://fonts.googleapis.com/css2?family=Source+Sans+3:ital,wght@0,400;0,600;1,400;1,600&family=Oswald:wght@300&display=swap">
<style>
  :root {
    --page-bg: #f2f2f2;
    --paper: #ffffff;
    --black: #231f20;
    --red: #e8423f;
    --ink: #2a2a2a;
    --title-pink: #f6c9c6;
    --rule: #b5b5b5;
    --photo-warm: #c9a070;
    --photo-dark: #2b2622;
  }
  * { margin: 0; padding: 0; box-sizing: border-box; }
  html, body { width: 1200px; height: 1000px; overflow: hidden; background: var(--page-bg); }
  body { position: relative; font-family: "Source Sans 3", Arial, sans-serif; color: var(--ink); }

  .back-cover {
    position: absolute; left: 300px; top: 40px;
    width: 600px; height: 920px;
    background: var(--paper);
    box-shadow: 0 2px 10px rgba(0,0,0,0.12);
    overflow: hidden;
  }
  .quote-band {
    position: absolute; left: 0; top: 0; width: 600px; height: 150px;
    background: var(--black);
    display: flex; align-items: center; justify-content: center;
    padding: 0 30px;
  }
  .quote-band p {
    color: #fff; font-style: italic; font-size: 25px; line-height: 1.28;
    text-align: center;
  }
  .red-swoop { position: absolute; left: 0; top: 150px; width: 600px; height: 170px; }

  .description {
    position: absolute; left: 16px; top: 290px; width: 232px;
    font-size: 9.3px; line-height: 1.3; text-align: justify;
  }
  .description p + p { margin-top: 10px; }

  .spheres { position: absolute; left: 22px; top: 684px; width: 214px; height: 205px; }
  .spheres text { font-family: "Source Sans 3", Arial, sans-serif; fill: #333; }

  .column-rule { position: absolute; top: 290px; width: 1px; height: 600px; background: var(--rule); }
  .column-rule.left { left: 264px; }

  .spine-title {
    position: absolute; left: 280px; top: 290px; height: 470px; width: 60px;
    font-family: "Oswald", "Arial Narrow", sans-serif; font-weight: 300;
    font-size: 56px; letter-spacing: 3px; color: var(--title-pink);
    writing-mode: vertical-rl; transform: rotate(180deg);
    text-align: center; line-height: 60px; white-space: nowrap;
  }

  .isbn-box {
    position: absolute; left: 278px; top: 768px; width: 80px; height: 86px;
    border: 1px solid #555;
    display: flex; align-items: center; justify-content: center;
    font-size: 7px; text-align: center; line-height: 1.3; text-transform: uppercase;
  }

  .author { position: absolute; left: 360px; top: 288px; width: 162px; }
  .author-name { color: var(--red); font-size: 25px; font-weight: 400; line-height: 1.05; }
  .author-bio { margin-top: 10px; font-size: 9.2px; line-height: 1.28; text-align: justify; }
  .author-site { margin-top: 10px; color: var(--red); font-size: 10px; letter-spacing: 2.6px; }

  .author-photo {
    position: absolute; left: 362px; top: 643px; width: 160px; height: 200px;
    background: linear-gradient(180deg, var(--photo-warm) 0%, #8a6a4a 45%, var(--photo-dark) 100%);
  }
</style>
</head>
<body>
  <section class="back-cover">
    <header class="quote-band">
      <p>“Rising Stride is THE guidebook that has the power to take your career and life in the direction that will prepare you for continued success.”</p>
    </header>

    <svg class="red-swoop" viewBox="0 0 600 170" aria-hidden="true">
      <path d="M0 0 H600 V45 C470 45 345 80 300 160 C255 80 130 45 0 45 Z" fill="var(--red)"/>
    </svg>

    <div class="description">
      <p>Celebrity conditioning specialist and trainer consultant, Tavo Minardi, offers powerful business ideas that are designed to transform the fitness professional’s career and life. Discover essential strategies that every trainer and entrepreneur should know, and the common mistakes to avoid. Identify the deeper meaning and purpose of your career by working smarter rather than harder.</p>
      <p>Find out how to create a brand, advertise it, and target your market. Create buzz by landing magazine press. Build celebrity clientele. Explore the world of multi-media projects, including TV appearances. Determine what to do when you finally reach your goals. “Rising Stride” is an opportunity for trainers to capture a share of the fitness industry’s vast $27 billion market. Reach your highest earning potential, understand your personal definition of success, and learn how to achieve it. Discover what you love to do, what you do well, what the fitness industry needs, and what it will pay for.</p>
      <p>Designed for trainers who want to establish habits that enhance their careers and set them apart from the rest, “Rising Stride” has the power to guide you upwards toward continued success. Use these business ideas to augment your passive income, generate multiple streams of revenue and increase your investments, resulting in more freedom and access in the fitness industry and beyond. Let “Rising Stride” unleash your potential to be a successful trainer.</p>
    </div>

    <svg class="spheres" viewBox="0 0 240 230" role="img" aria-label="Four spheres of success diagram">
      <ellipse cx="122" cy="62" rx="52" ry="56" fill="#7fb6dc" fill-opacity="0.8" stroke="#5a8fb5" stroke-width="0.6"/>
      <ellipse cx="66" cy="138" rx="64" ry="42" fill="#f39a78" fill-opacity="0.75" stroke="#c77a5c" stroke-width="0.6"/>
      <ellipse cx="178" cy="122" rx="60" ry="48" fill="#b9d98c" fill-opacity="0.7" stroke="#8fb068" stroke-width="0.6"/>
      <ellipse cx="118" cy="182" rx="50" ry="46" fill="#f7e68a" fill-opacity="0.7" stroke="#c9b860" stroke-width="0.6"/>
      <ellipse cx="122" cy="128" rx="50" ry="38" fill="#6f8f6a" fill-opacity="0.75" stroke="#4d6a4a" stroke-width="0.8"/>
      <text x="122" y="32" font-size="8" text-anchor="middle">What you love</text>
      <text x="38" y="142" font-size="8" text-anchor="middle">What you do well</text>
      <text x="206" y="118" font-size="8" text-anchor="middle">What the world</text>
      <text x="206" y="128" font-size="8" text-anchor="middle">needs</text>
      <text x="118" y="198" font-size="8" text-anchor="middle">What the world</text>
      <text x="118" y="208" font-size="8" text-anchor="middle">will pay for</text>
      <text x="122" y="133" font-size="14" font-weight="600" text-anchor="middle" fill="#1e1e1e">SUCCESS</text>
    </svg>

    <div class="column-rule left"></div>

    <div class="spine-title">RISING STRIDE</div>

    <div class="isbn-box">Reserved for<br>ISBN number &amp; barcode</div>

    <div class="author">
      <h2 class="author-name">Tavo<br>Minardi, CSCS</h2>
      <p class="author-bio">Hollywood trainer Tavo Minardi, CSCS is a professional fitness consultant and creator of the popular “Ember” technique and brand. His clients include celebrities, pro athletes, musicians, fashion models and political figures. Recognizing his expertise, top publications including Pulse, Verve, Ascent, Home Circle, Pure Plate and Spotlight have featured Minardi as a highly sought-after fitness authority. Kelvo magazine describes his DVD TavoMove as “a workout you’ll look forward to.” Minardi appeared on a Norvex commercial aired during the Global Cup, and he is also the co-developer of a natural energy drink that increases power and metabolism with an ancient Peruvian superfood. Minardi’s fitness expertise is complemented by his education in finance and advertising, and he has guided numerous trainers and brands towards their maximum earning potential.</p>
      <p class="author-site">www.BrenoVigor.net</p>
    </div>

    <div class="author-photo" role="img" aria-label="Portrait photo of the author seated against a sunset city skyline"></div>
  </section>
</body>
</html>
```